Morden, Creative, Unique, Independent Wine Shop

1. We are a brand new wine shop located in Melbourne Australia, we have our logo already, simply use the logo to design a business card.
2. I have uploaded our logo in two versions, with or without shadow, any of them is acceptable.
3. Make it as creative and unique as possible, no limitation of shape, color combination, geometry pattern, fonts, composing etc.
3. Info on the card:
- Brambleford Wine Cellar (Not very necessary if logo is obviously shown)
- 42 Ferncastle Steet, Hampton, Victoria, Australia 3188
- +61 3 9018 4637
- www.bramblefordwinecellar.com.au
- bramblefordwinecellar@mailvista.com
- Additional icons: Google, Instagram, Facebook, Twitter
4. Once again, forget it is a commercial card, make it special.

```html
<!DOCTYPE html>
<html lang="en">
<head>
<meta charset="utf-8">
<title>Brambleford Wine Cellar – Business Card</title>
<link rel="stylesheet" href="https://fonts.googleapis.com/css2?family=Roboto:wght@400;500;700&display=swap">
<style>
  :root {
    --wine: #a91e3f;
    --paper: #ffffff;
    --ink-grey: #6b6b6b;
    --text-grey: #7a7a7a;
    --rule: #bdbdbd;
    --stage: #2c2c2e;
  }
  * { margin: 0; padding: 0; box-sizing: border-box; }
  html, body { width: 1200px; height: 904px; overflow: hidden; }
  body {
    background: var(--stage);
    font-family: "Roboto", Arial, sans-serif;
    position: relative;
  }
  .card {
    position: absolute;
    left: 250px;
    width: 700px;
    height: 400px;
    border-radius: 3px;
  }
  .card--front { top: 40px; background: var(--wine); }
  .card--back { top: 464px; background: var(--paper); }

  .brand {
    position: absolute;
    display: flex;
    align-items: center;
    gap: 16px;
    font-family: "Roboto", Arial, sans-serif;
    font-weight: 500;
    line-height: 1.05;
    letter-spacing: 0.04em;
  }
  .brand__dot { border-radius: 50%; flex: none; }
  .card--front .brand {
    left: 50%; top: 50%; transform: translate(-50%, -50%);
    color: var(--paper); font-size: 40px;
  }
  .card--front .brand__dot { width: 70px; height: 70px; background: var(--paper); }
  .card--back .brand {
    left: 48px; top: 50%; transform: translateY(-50%);
    color: var(--wine); font-size: 24px;
  }
  .card--back .brand__dot { width: 48px; height: 48px; background: var(--wine); }

  .divider {
    position: absolute;
    left: 345px; top: 80px;
    width: 1px; height: 240px;
    background: var(--rule);
  }
  .details {
    position: absolute;
    left: 375px; top: 82px;
    width: 300px;
    color: var(--text-grey);
  }
  .details__name { color: var(--wine); font-weight: 700; font-size: 27px; line-height: 1.1; }
  .details__role { font-size: 20px; margin-top: 2px; color: var(--ink-grey); }
  .details__address { font-size: 14px; line-height: 1.35; margin-top: 22px; }
  .contacts { list-style: none; margin-top: 20px; font-size: 14px; line-height: 1.45; }
  .contacts li { display: flex; align-items: center; gap: 8px; }
  .contacts svg { width: 11px; height: 11px; fill: var(--wine); flex: none; }
  .contacts .web-accent { color: var(--wine); }

  .social {
    position: absolute;
    right: 30px; bottom: 30px;
    display: flex; gap: 5px;
  }
  .social span { width: 18px; height: 18px; border-radius: 3px; background: var(--wine); }
</style>
</head>
<body>
  <section class="card card--front" aria-label="Card front">
    <div class="brand"><span class="brand__dot"></span><span>Brambleford<br>Wine Cellar</span></div>
  </section>

  <section class="card card--back" aria-label="Card back">
    <div class="brand"><span class="brand__dot"></span><span>Brambleford<br>Wine Cellar</span></div>
    <div class="divider"></div>
    <div class="details">
      <p class="details__name">Daniel Whitmore</p>
      <p class="details__role">Manager</p>
      <p class="details__address">42 Ferncastle Steet, Hampton<br>Victoria, Australia 3188</p>
      <ul class="contacts">
        <li><svg viewBox="0 0 24 24" aria-hidden="true"><path d="M6.6 10.8a15.1 15.1 0 0 0 6.6 6.6l2.2-2.2a1 1 0 0 1 1-.25 11.4 11.4 0 0 0 3.6.57 1 1 0 0 1 1 1V20a1 1 0 0 1-1 1A17 17 0 0 1 3 4a1 1 0 0 1 1-1h3.5a1 1 0 0 1 1 1c0 1.25.2 2.45.57 3.6a1 1 0 0 1-.25 1z"/></svg>+61 3 9018 4637</li>
        <li><svg viewBox="0 0 24 24" aria-hidden="true"><path d="M2 5h20v14H2z M2 5l10 8 10-8" /></svg>bramblefordwinecellar@mailvista.com</li>
        <li><svg viewBox="0 0 24 24" aria-hidden="true"><circle cx="12" cy="12" r="10"/></svg>www.<span class="web-accent">bramblefordwinecellar</span>.com.au</li>
      </ul>
    </div>
    <div class="social" aria-label="Social links">
      <span></span><span></span><span></span><span></span>
    </div>
  </section>
</body>
</html>
```